Ridgeway Spectral Studies Website

We are a paranormal research group located in Central Mississippi. We are a group dedicated to help the community in any paranormal investigation. We use fresh new techniques with cutting edge technology to investigate any paranormal situation. Our services are always free of charge to anyone. An unique feature of our group is that we provide a complete history of the property, courtesy of our research team. We would like to see designs that incorporate our logo. We are a professional group and want a professional website.. we will need a home page that will reflect out goals. Links will include "Home, About Us, Contact us, (MAYBE MORE). We will also want a "blank page" with same links that we can edit and fill in all the information..

Target Market(s)

Paranormal-Ghost hunting groups

Industry/Entity Type

Community

Coding

Coded - Design and coding required

Number of Pages Required

2 page

Font styles to use
Other font styles liked:

Requirements
Must have
• we will need a home page that will reflect out goals. Links will include "Home, About Us, Contact us, (MAYBE MORE). We will also want a "blank page" with same links that we can edit and fill in all the information..

```html
<!DOCTYPE html>
<html lang="en">
<head>
<meta charset="utf-8">
<title>Ridgeway Spectral Studies – Home</title>
<link rel="stylesheet" href="https://fonts.googleapis.com/css2?family=Cabin+Sketch:wght@700&family=Rubik+Dirt&family=Roboto:wght@400;500&display=swap">
<style>
:root{
  --night:#03060c;
  --header-blue:#1c3352;
  --header-deep:#060b14;
  --cloud:#1a2638;
  --cloud-deep:#070b12;
  --blood:#e3141b;
  --blood-dark:#8e0a0e;
  --ink:#ffffff;
  --muted:#d9dde3;
  --panel:rgba(8,12,20,.78);
  --footer:#020305;
}
*{margin:0;padding:0;box-sizing:border-box}
html,body{width:1097px;height:1200px;overflow:hidden;background:var(--night)}
.page{position:relative;width:1097px;height:1200px;overflow:hidden;
  background:radial-gradient(ellipse 520px 260px at 120px 640px,#1f2d42 0%,transparent 70%),
             radial-gradient(ellipse 480px 300px at 900px 620px,#1c2940 0%,transparent 70%),
             radial-gradient(ellipse 600px 280px at 500px 900px,#16233a 0%,transparent 70%),
             linear-gradient(180deg,var(--cloud) 0%,var(--cloud-deep) 100%);
  font-family:"Roboto",sans-serif;color:var(--ink)}
.site-header{position:absolute;left:0;top:0;width:1097px;height:129px;
  background:radial-gradient(ellipse 420px 160px at 200px 60px,var(--header-blue) 0%,var(--header-deep) 80%)}
.brand{position:absolute;left:150px;top:44px;display:flex;align-items:center;gap:10px}
.brand-mark{width:34px;height:34px;border-radius:50%;background:var(--muted)}
.brand-name{font-family:"Cabin Sketch",sans-serif;font-weight:700;font-size:17px;line-height:1.1;width:120px;color:var(--ink)}
.main-nav{position:absolute;top:52px;left:0;font-family:"Cabin Sketch",sans-serif;font-weight:700;font-size:20px}
.main-nav a{position:absolute;white-space:nowrap;color:var(--ink);text-decoration:none}
.main-nav a.is-current{color:var(--blood)}
.hero{position:absolute;left:3px;top:130px;width:1091px;height:394px;border:2px solid #222}
.hero-scene{position:absolute;inset:0;
  background:radial-gradient(ellipse 260px 220px at 560px 200px,#8994b4 0%,#4a5a8a 40%,transparent 75%),
             radial-gradient(ellipse 300px 200px at 200px 330px,#3b4a78 0%,transparent 70%),
             linear-gradient(180deg,#2b3456 0%,#141a2e 60%,#04060b 100%)}
.hero-title{position:absolute;left:173px;top:142px;font-family:"Rubik Dirt",sans-serif;font-size:42px;line-height:48px;font-weight:400}
.hero-title .line-1{color:var(--ink);display:block}
.hero-title .line-2{color:var(--blood);display:block}
.hero-arrow{position:absolute;top:158px}
.intro{position:absolute;left:155px;top:536px;width:775px;height:210px;background:var(--panel)}
.intro-brand{position:absolute;left:14px;top:70px;width:140px;display:flex;flex-direction:column;align-items:center;gap:8px;text-align:center}
.intro-brand .brand-mark{width:44px;height:44px;background:#e1c23a}
.intro-brand .brand-name{width:140px;text-align:center;font-size:16px}
.section-title{font-family:"Cabin Sketch",sans-serif;font-weight:700;color:var(--blood);font-size:24px;line-height:28px;letter-spacing:1px}
.copy{font-size:12px;line-height:23.5px;color:var(--muted)}
.copy .line{display:block;white-space:nowrap}
.intro .section-title{position:absolute;left:178px;top:20px}
.intro .copy{position:absolute;left:178px;top:55px;width:600px}
.read-more{position:absolute;display:block;width:116px;height:34px;line-height:34px;text-align:center;
  font-weight:500;font-size:14px;color:var(--ink);text-decoration:none;background:var(--blood);border-radius:14px 4px 16px 5px;
  box-shadow:inset 0 0 6px var(--blood-dark)}
.intro .read-more{left:175px;top:160px}
.stories .section-title{position:absolute;left:168px;top:796px}
.stories .copy{position:absolute;left:168px;top:833px;width:361px}
.stories .copy .line{text-align:justify;text-align-last:justify}
.stories .read-more{left:166px;top:991px}
.video-frame{position:absolute;left:548px;top:787px;width:393px;height:243px;background:var(--blood);
  border:3px solid var(--blood-dark);border-radius:3px;box-shadow:0 0 8px rgba(227,20,27,.5)}
.video-still{position:absolute;left:14px;top:13px;width:361px;height:184px;
  background:radial-gradient(ellipse 200px 100px at 150px 40px,#8d9488 0%,transparent 70%),
             linear-gradient(180deg,#5c6360 0%,#4a4f47 55%,#2f322d 100%)}
.video-play{position:absolute}
.video-controls{position:absolute;left:14px;top:197px;width:361px;height:32px;background:#111}
.site-footer{position:absolute;left:0;top:1101px;width:1097px;height:99px;background:var(--footer);border-top:2px solid var(--blood-dark)}
.footer-links{position:absolute;left:160px;top:28px;font-size:13px;color:var(--ink)}
.footer-links a{color:var(--ink);text-decoration:none}
.copyright{position:absolute;left:158px;top:54px;font-size:13px}
.social{position:absolute;left:827px;top:38px;display:flex;gap:5px}
.social span{width:24px;height:24px;border-radius:50%;background:var(--ink)}
.social span:first-child{background:#55acee}
</style>
</head>
<body>
<div class="page">
  <header class="site-header">
    <div class="brand"><span class="brand-mark"></span><span class="brand-name">Ridgeway Spectral Studies</span></div>
    <nav class="main-nav">
      <a class="is-current" href="#" style="left:470px">Home</a>
      <a href="#" style="left:572px">About us</a>
      <a href="#" style="left:693px">Your Stories</a>
      <a href="#" style="left:842px">Contact us</a>
    </nav>
  </header>

  <section class="hero">
    <div class="hero-scene" role="img" aria-label="Haunted Victorian house among bare trees under a stormy moonlit sky with bats"></div>
    <h1 class="hero-title"><span class="line-1">PARANORMAL</span><span class="line-2">INVESTIGATION</span></h1>
    <svg class="hero-arrow" style="left:68px" width="32" height="62" viewBox="0 0 32 62"><polyline points="30,2 2,31 30,60" fill="none" stroke="#fff" stroke-width="1.5"/></svg>
    <svg class="hero-arrow" style="left:976px" width="32" height="62" viewBox="0 0 32 62"><polyline points="2,2 30,31 2,60" fill="none" stroke="#fff" stroke-width="1.5"/></svg>
  </section>

  <section class="intro">
    <div class="intro-brand"><span class="brand-mark"></span><span class="brand-name">Ridgeway Spectral Studies</span></div>
    <h2 class="section-title">WELCOME TO RSS</h2>
    <p class="copy">
      <span class="line">Lorem Ipsum is simply dummy text of the printing and typesetting industry. Lorem Ipsum has been the</span>
      <span class="line">industry's standard dummy text ever since the 1500s, when an unknown printer took a galley of type and</span>
      <span class="line">scrambled it to make a type specimen book. It has survived not only five centuries, but also the leap into</span>
      <span class="line">electronic typesetting, remaining essentially unchanged. It was popularised in the 1960s with the release</span>
    </p>
    <a class="read-more" href="#">Read More</a>
  </section>

  <section class="stories">
    <h2 class="section-title">YOUR STORIES</h2>
    <p class="copy">
      <span class="line">Lorem Ipsum is simply dummy text of the printing and typeset-</span>
      <span class="line">ting industry. Lorem Ipsum has been the industry's standard</span>
      <span class="line">dummy text ever since the 1500s, when an unknown printer took</span>
      <span class="line">a galley of type and scrambled it to make a type specimen book.</span>
      <span class="line">It has survived not only five centuries, but also the leap into elec-</span>
      <span class="line">tronic typesetting, remaining essentially unchanged. It was</span>
    </p>
    <a class="read-more" href="#">Read More</a>
    <div class="video-frame">
      <div class="video-still" role="img" aria-label="Video still of an old graveyard with weathered headstones and a gothic tower under storm clouds"></div>
      <svg class="video-play" style="left:177px;top:83px" width="40" height="40" viewBox="0 0 40 40"><circle cx="20" cy="20" r="20" fill="rgba(40,40,40,.8)"/><polygon points="15,11 29,20 15,29" fill="#fff"/></svg>
      <svg class="video-controls" width="361" height="32" viewBox="0 0 361 32">
        <circle cx="22" cy="16" r="7" fill="none" stroke="#fff" stroke-width="1.5"/><polygon points="20,12 26,16 20,20" fill="#fff"/>
        <polygon points="47,14 50,14 54,11 54,21 50,18 47,18" fill="#e3141b"/>
        <g fill="#e3141b"><rect x="58" y="12" width="2" height="8"/><rect x="62" y="12" width="2" height="8"/><rect x="66" y="12" width="2" height="8"/><rect x="70" y="12" width="2" height="8"/></g>
        <g fill="#666"><rect x="74" y="12" width="2" height="8"/><rect x="78" y="12" width="2" height="8"/></g>
        <rect x="91" y="15" width="158" height="2" fill="#555"/><rect x="91" y="15" width="55" height="2" fill="#e3141b"/>
        <text x="261" y="19" fill="#ddd" font-size="7.5" font-family="Roboto,sans-serif">01:30 / 04:55</text>
        <rect x="318" y="12" width="10" height="8" fill="none" stroke="#fff" stroke-width="1.5"/>
        <circle cx="340" cy="16" r="4" fill="none" stroke="#fff" stroke-width="2.5" stroke-dasharray="2 1.2"/>
      </svg>
    </div>
  </section>

  <footer class="site-footer">
    <p class="footer-links"><a href="#">Privacy Policy</a> | <a href="#">Terms Conditions</a> | <a href="#">Sitemap</a> | <a href="#">Contact Us</a></p>
    <p class="copyright">Copyright © 2014&nbsp; All Rights Reserved</p>
    <div class="social"><span></span><span></span><span></span><span></span></div>
  </footer>
</div>
</body>
</html>
```